Women's Health Company needs business card

We need a business card for a USA based women's health care company. We use digital technology to enhance therapy prescribed by clinicians for their patients

```html
<!DOCTYPE html>
<html lang="en">
<head>
<meta charset="UTF-8">
<title>Norvia Health – Business Card</title>
<link href="https://fonts.googleapis.com/css2?family=Montserrat:wght@400;500;700&display=swap" rel="stylesheet">
<style>
  :root {
    --backdrop: #2b2b2d;
    --purple: #5b2d85;
    --purple-deep: #4f2577;
    --purple-tone: #6e43a0;
    --teal: #6fbdb7;
    --ink: #2e2e33;
    --paper: #ffffff;
  }
  * { margin: 0; padding: 0; box-sizing: border-box; }
  html, body {
    width: 1200px;
    height: 1186px;
    overflow: hidden;
    background: var(--backdrop);
    font-family: "Montserrat", sans-serif;
  }
  .sheet {
    width: 1200px;
    height: 1186px;
    display: flex;
    flex-direction: column;
    align-items: center;
    justify-content: center;
    gap: 60px;
  }
  .card {
    width: 900px;
    height: 514px;
    border-radius: 34px;
    position: relative;
    overflow: hidden;
  }

  /* Back side */
  .card-back {
    background: linear-gradient(135deg, var(--purple-tone) 0%, var(--purple) 45%, var(--purple-deep) 100%);
    display: flex;
    align-items: center;
    justify-content: center;
    gap: 22px;
  }
  .card-back .brand-dot {
    width: 22px; height: 22px; border-radius: 50%;
    background: #7a55a8;
  }
  .card-back .brand-name {
    font-size: 68px;
    font-weight: 500;
    color: #7a55a8;
    letter-spacing: 1px;
  }

  /* Front side */
  .card-front {
    background: var(--paper);
  }
  .front-brand {
    position: absolute;
    left: 60px;
    top: 0;
    width: 440px;
    height: 100%;
    display: flex;
    align-items: center;
    gap: 14px;
  }
  .front-brand .brand-dot {
    width: 14px; height: 14px; border-radius: 50%;
    background: var(--teal);
  }
  .front-brand .brand-name {
    font-size: 46px;
    font-weight: 500;
    color: var(--teal);
  }
  .divider {
    position: absolute;
    left: 515px;
    top: 130px;
    width: 2px;
    height: 260px;
    background: var(--teal);
  }
  .contact {
    position: absolute;
    left: 550px;
    top: 130px;
    color: var(--ink);
  }
  .contact .person-name {
    font-size: 30px;
    font-weight: 700;
    color: var(--teal);
    line-height: 1.1;
  }
  .contact .person-role {
    font-size: 17px;
    font-weight: 400;
    margin-top: 4px;
  }
  .contact-list {
    list-style: none;
    margin-top: 26px;
  }
  .contact-list li {
    display: flex;
    align-items: center;
    gap: 12px;
    font-size: 17px;
    line-height: 26px;
  }
  .contact-list svg { width: 16px; height: 16px; flex: none; }
  .address {
    margin-top: 22px;
    font-size: 17px;
    line-height: 24px;
  }
</style>
</head>
<body>
<main class="sheet">
  <section class="card card-back" aria-label="Card back">
    <span class="brand-dot"></span>
    <span class="brand-name">Norvia Health</span>
  </section>

  <section class="card card-front" aria-label="Card front">
    <div class="front-brand">
      <span class="brand-dot"></span>
      <span class="brand-name">Norvia Health</span>
    </div>
    <div class="divider"></div>
    <div class="contact">
      <p class="person-name">Clara Weston</p>
      <p class="person-role">Owner</p>
      <ul class="contact-list">
        <li>
          <svg viewBox="0 0 16 16" aria-hidden="true"><path fill="#6fbdb7" d="M3 1.5h3l1.2 3.2-1.7 1.1a8 8 0 0 0 4.7 4.7l1.1-1.7 3.2 1.2v3a1.5 1.5 0 0 1-1.6 1.5A13 13 0 0 1 1.5 3.1 1.5 1.5 0 0 1 3 1.5z"/></svg>
          +49 401 555 0182
        </li>
        <li>
          <svg viewBox="0 0 16 16" aria-hidden="true"><rect x="1" y="3" width="14" height="10" rx="1.5" fill="#6fbdb7"/><path d="M1.5 4l6.5 5 6.5-5" fill="none" stroke="#fff" stroke-width="1.3"/></svg>
          info@norviahealth.com
        </li>
        <li>
          <svg viewBox="0 0 16 16" aria-hidden="true"><circle cx="8" cy="8" r="6.5" fill="none" stroke="#6fbdb7" stroke-width="1.5"/><ellipse cx="8" cy="8" rx="2.8" ry="6.5" fill="none" stroke="#6fbdb7" stroke-width="1.2"/><path d="M1.5 8h13" stroke="#6fbdb7" stroke-width="1.2"/></svg>
          www.norviahealth.com
        </li>
      </ul>
      <p class="address">Lindenallee 42<br>20259 Hamburg</p>
    </div>
  </section>
</main>
</body>
</html>
```